Cosmetics Brand Logo and Bottle Label Design

We are creating a new cosmetics brand called "Nolan Whitby" and would like you to create an amazing logo and bottle label for this brand's new 100% pure argan oil product.
For the logo, we really like the logo's of Marin Calloway and Vessa. The text should be Sans Serif (without feet).
For the actual bottle label, please find attached labels of one of our competitors design which really like. We really like the simplicity and elegance of the design. The only difference is that our product will be using light turqoise as the brand color. Please feel free to add your own creativity into it as well.
Industry/Entity Type
Cosmetics
Logo Text
Nolan Whitby
Font styles to use

```html
<!DOCTYPE html>
<html lang="en">
<head>
<meta charset="utf-8">
<title>Nolan Whitby — Pure Argan Oil Box Front</title>
<link href="https://fonts.googleapis.com/css2?family=Open+Sans:wght@300;400;700&display=swap" rel="stylesheet">
<style>
  :root {
    --teal: #3ab3a5;
    --teal-soft: #7fcfc5;
    --ink: #1f2725;
    --panel: #eef0f1;
    --backdrop: #c9ccd0;
    --cream: #f3f1e8;
  }
  * { box-sizing: border-box; margin: 0; padding: 0; }
  html, body { width: 1200px; height: 1200px; overflow: hidden; }
  body {
    background: var(--backdrop);
    font-family: "Open Sans", sans-serif;
    position: relative;
  }
  .box-front {
    position: absolute;
    left: 400px; top: 45px;
    width: 400px; height: 1110px;
    background: var(--panel);
  }
  .natural-seal {
    position: absolute;
    left: 111px; top: 40px;
    width: 178px; height: 178px;
    border: 3px solid var(--teal);
    border-radius: 50%;
    color: var(--teal);
    display: flex; flex-direction: column; align-items: center; justify-content: center;
    transform: rotate(-12deg);
  }
  .natural-seal .percent { font-size: 54px; font-weight: 300; line-height: 1; }
  .natural-seal .word { font-size: 34px; font-weight: 300; line-height: 1.1; }
  .brand-badge {
    position: absolute;
    left: 33px; top: 358px;
    width: 338px; height: 338px;
    border-radius: 50%;
    background: var(--ink);
    border: 14px solid var(--teal);
    display: flex; flex-direction: column; align-items: center; justify-content: center;
    color: var(--cream);
  }
  .brand-name {
    font-size: 40px; font-weight: 300;
    line-height: 1.15; text-align: center;
  }
  .brand-tagline {
    margin-top: 22px;
    font-size: 21px; font-weight: 300; letter-spacing: 0.5px;
  }
  .copy {
    position: absolute;
    left: 45px; top: 758px; width: 236px;
    color: var(--teal);
  }
  .copy .kicker { font-size: 14px; font-weight: 700; line-height: 17px; }
  .copy .headline { font-size: 30px; font-weight: 700; line-height: 33px; letter-spacing: -0.3px; white-space: nowrap; }
  .copy .subhead { font-size: 19px; font-weight: 400; line-height: 21px; }
  .copy .body { font-size: 10.4px; line-height: 12.5px; }
  .benefit-icons {
    position: absolute;
    left: 47px; top: 932px;
    display: flex; gap: 17px;
  }
  .benefit {
    width: 92px; height: 92px;
    border-radius: 50%;
    border: 2px solid var(--teal);
    display: flex; align-items: center; justify-content: center;
  }
  .benefit .placeholder {
    width: 76px; height: 76px; border-radius: 50%;
    background: radial-gradient(circle at 40% 40%, var(--teal-soft), var(--teal));
  }
</style>
</head>
<body>
  <main class="box-front">
    <div class="natural-seal">
      <span class="percent">100%</span>
      <span class="word">natural</span>
    </div>

    <div class="brand-badge">
      <div class="brand-name">Nolan<br>Whitby</div>
      <div class="brand-tagline">pure argan oil</div>
    </div>

    <section class="copy">
      <p class="kicker">LOREM IPSUM</p>
      <h1 class="headline">DOLOR SIT AMET</h1>
      <p class="subhead">SAMPLE TEXT</p>
      <p class="body">Lorem ipsum dolor sit amet, consectetuer adipiscing elit, sed diam nonummy nibh euismod tincidunt ut laoreet dolore magna aliquam erat volutpat. Lorem ipsum dolor sit amet, consectetuer adipiscing elit, sed diam nonummy nibh euismod tincidunt ut laoreet dolore magna aliquam erat volutpat.</p>
    </section>

    <div class="benefit-icons">
      <div class="benefit"><div class="placeholder" role="img" aria-label="Benefit icon: glowing skin in profile"></div></div>
      <div class="benefit">
        <svg width="50" height="62" viewBox="0 0 50 62" aria-hidden="true">
          <path d="M25 2 C25 2 4 28 4 40 A21 21 0 0 0 46 40 C46 28 25 2 25 2 Z" fill="var(--teal)"/>
          <path d="M34 38 A10 10 0 0 1 28 50" fill="none" stroke="var(--panel)" stroke-width="3" stroke-linecap="round"/>
        </svg>
      </div>
      <div class="benefit"><div class="placeholder" role="img" aria-label="Benefit icon: cut aloe leaf"></div></div>
    </div>
  </main>
</body>
</html>
```